Tri-fold Brochure Design for Law Firm

I need a tri-fold brochure to give to prospective clients.
I have attached a Photoshop design file of a tri-fold brochure. The content (copy) is good, however, he brochure itself looks very amateurish.
I want a professional, sophisticated looking brochure.
The law firm specializes in commercial debt collection.
The law firm is located in New York City.
Our target market is business owners, doctors, lawyers, collection agencies and accountants.
Visit my website which is being designed at www.dornvek.com. I like the font used for the name of my company and the rich blue color used.

Target Market(s)

Business Owners, Doctors, Law Firms and Accountants

Industry/Entity Type

Law Firm

Font styles to use
Serif

Requirements
Must have
• Professional quality graphic work. Attention to details.
• PHOTOGRAPHS ONLY, NO CLIP-ART.
• DARK COLORS - NAVY BLUE, HUNTER GREEN, BLACK, GRAY & WHITE
Nice to have
• I want it to look smart, modern and sophisticated.
• Visit my website which is being designed at www.dornvek.com. I like the font used for the name of my company and the rich blue color used.
Should not have
• Bad artwork
• CLIP ART

```html
<!DOCTYPE html>
<html lang="en">
<head>
<meta charset="utf-8">
<title>Dornvek Tri-fold Brochure</title>
<link href="https://fonts.googleapis.com/css2?family=Open+Sans:ital,wght@0,400;0,600;0,700;1,400&family=Roboto:wght@500;700;900&display=swap" rel="stylesheet">
<style>
  :root {
    --navy: #1d2a6b;
    --navy-deep: #141c4d;
    --blue: #0f8ee0;
    --blue-bright: #1fa8f2;
    --sky: #3cc0ff;
    --ink: #1b1b24;
    --paper: #ffffff;
    --backdrop: #9a9a9c;
    --photo-brown: #6b4a2c;
    --photo-gold: #c29a5a;
  }
  * { box-sizing: border-box; margin: 0; padding: 0; }
  html, body { width: 1200px; height: 800px; overflow: hidden; }
  body {
    background: var(--backdrop);
    font-family: "Open Sans", Arial, sans-serif;
    color: var(--ink);
  }
  .brochure {
    position: absolute; left: 30px; top: 30px;
    width: 1140px; height: 740px;
    display: flex;
    box-shadow: 0 10px 30px rgba(0,0,0,.35);
  }
  .panel { position: relative; width: 380px; height: 740px; overflow: hidden; }
  .panel p, .panel li { font-size: 11.2px; line-height: 1.42; }
  .panel-heading {
    font-family: "Roboto", Arial, sans-serif;
    font-weight: 900; text-transform: uppercase; letter-spacing: .2px;
  }
  /* left panel */
  .panel--about { background: var(--paper); padding: 24px 28px 0; }
  .statue-photo {
    position: absolute; left: 0; bottom: 56px; width: 230px; height: 250px;
    background: radial-gradient(ellipse at 40% 40%, rgba(150,140,160,.35), rgba(200,195,210,.15) 60%, rgba(255,255,255,0) 80%);
  }
  .section { position: relative; text-align: center; }
  .section + .section { margin-top: 16px; }
  .icon-badge {
    width: 66px; height: 66px; border-radius: 50%; background: var(--blue);
    margin: 0 auto 8px; display: flex; align-items: center; justify-content: center;
  }
  .rule-heading {
    display: flex; align-items: center; justify-content: center; gap: 10px;
    font-size: 19px; margin-bottom: 10px; color: var(--navy);
  }
  .rule-heading::before, .rule-heading::after {
    content: ""; width: 42px; height: 2px; background: var(--blue);
  }
  .accent { color: var(--blue-bright); }
  .section p { text-align: left; }
  .section p + p { margin-top: 8px; }
  .url-band {
    position: absolute; left: 0; right: 0; bottom: 0; height: 56px;
    background: var(--blue-bright); color: #fff;
    display: flex; align-items: center; justify-content: center;
    font-size: 18px; letter-spacing: 4px;
  }
  /* middle panel */
  .panel--fees {
    background: linear-gradient(170deg, var(--navy-deep) 0%, #1e3a8a 14%, var(--blue) 32%, var(--blue-bright) 70%);
    color: #fff; padding: 28px 30px 0;
  }
  .fees-heading { font-size: 21px; margin-bottom: 12px; }
  .fees-heading .accent { color: var(--sky); }
  .fees-heading--navy .accent { color: var(--navy); }
  .fee-list { margin: 8px 0 18px 18px; }
  .panel--fees p + p { margin-top: 8px; }
  .court-photo {
    position: absolute; left: 0; bottom: 0; width: 380px; height: 200px;
  }
  /* right panel */
  .panel--advisory { background: var(--paper); padding: 28px 30px 0; }
  .navy-edge { position: absolute; right: 0; top: 0; width: 16px; height: 300px; background: var(--navy); }
  .advisory-heading { font-size: 20px; color: var(--navy); }
  .advisory-heading .accent { color: var(--blue-bright); }
  .advisory-sub {
    font-family: "Roboto", Arial, sans-serif; font-weight: 700; font-size: 13px;
    color: var(--navy); margin: 2px 0 8px;
  }
  .panel--advisory p + p { margin-top: 6px; }
  .ruled { display: flex; align-items: center; gap: 8px; margin: 16px 0 8px; font-size: 17px; }
  .ruled::after { content: ""; flex: 1; height: 2px; background: var(--blue); }
  .advisory-band { position: absolute; left: 0; bottom: 0; width: 380px; height: 110px; }
  .advisory-band span {
    position: absolute; right: 34px; bottom: 26px; color: #fff;
    font-size: 18px; letter-spacing: 4px;
  }
</style>
</head>
<body>
<div class="brochure">

  <section class="panel panel--about">
    <div class="statue-photo" role="img" aria-label="Faint photograph of a classical justice statue"></div>

    <div class="section">
      <div class="icon-badge">
        <svg width="38" height="34" viewBox="0 0 38 34" fill="none" stroke="#fff" stroke-width="2.4">
          <circle cx="15" cy="10" r="6"/><path d="M3 31c0-8 5-12 12-12s12 4 12 12z"/>
          <path d="M22 5a6 6 0 1 1 2 11M28 20c4 1 7 5 7 11h-6"/>
        </svg>
      </div>
      <h2 class="panel-heading rule-heading"><span><span class="accent">Who</span> We Are</span></h2>
      <p>MARLOW DORNVEK &amp; COMPANY, PLLC ("DORNVEK") is a New York based law firm devoted to the collection of accounts receivable and business debts.</p>
    </div>

    <div class="section">
      <div class="icon-badge">
        <svg width="36" height="36" viewBox="0 0 36 36" fill="none" stroke="#fff" stroke-width="3.4" stroke-linecap="round" stroke-linejoin="round">
          <path d="M7 19l7 7 15-16"/>
        </svg>
      </div>
      <h2 class="panel-heading rule-heading"><span><span class="accent">What</span> We Do</span></h2>
      <p>Within 24 to 72 hours of receiving a claim, we will verify the debt, investigate the Debtor, skip trace all known stakeholders and file a lawsuit with the intent of collecting the full amount due in the shortest time possible.</p>
      <p>We will use all legal means necessary to locate, identify, seize, or otherwise garnish a Debtor's assets and income, while always having an attorney available to speak directly with the Debtor to achieve an amicable resolution as quickly as possible.</p>
    </div>

    <div class="section">
      <div class="icon-badge">
        <svg width="38" height="38" viewBox="0 0 38 38" fill="none" stroke="#fff" stroke-width="2.6" stroke-linecap="round">
          <circle cx="17" cy="21" r="13"/><circle cx="17" cy="21" r="7.5"/><circle cx="17" cy="21" r="2" fill="#fff"/>
          <path d="M17 21L33 5M28 5h5v5"/>
        </svg>
      </div>
      <h2 class="panel-heading rule-heading"><span><span class="accent">Our</span> Mission</span></h2>
      <p>Our mission is to protect our clients' bottom line, while preserving their reputation. We recognize and appreciate that your Debtor was once a trusted customer and may be a source of future revenue. We treat all Debtors with respect, while aggressively seeking to collect all monies owed.</p>
    </div>

    <div class="url-band">www.dornvek.com</div>
  </section>

  <section class="panel panel--fees">
    <h2 class="panel-heading fees-heading">Flexible <span class="accent">Fee Structure</span></h2>
    <p>We recognize that each claim is unique, therefore to better serve our clients we offer a variety of fee structures that meet the needs of our clients. Including:</p>
    <ul class="fee-list">
      <li>Contingency Fee</li>
      <li>Flat Fee</li>
      <li>Hourly fee</li>
      <li>Monthly or Annual Retainer</li>
      <li>Any combination of the above</li>
    </ul>

    <h2 class="panel-heading fees-heading fees-heading--navy">Handling <span class="accent">Medical Receivables</span></h2>
    <p>Medical receivables require a soft touch.</p>
    <p>Doctors and health organizations often write-off tens of thousands of dollars in unpaid deductibles and co-insurance which are rightfully due them out of fear that pursuing these debts will alienate, upset or offend their patients.</p>
    <p>We offer non-legal, HIPAA compliant collection methods which can effectively and consistently turn these otherwise uncollectible assets into real cash.</p>
    <p>Using a combination of letters and phone calls, our staff contacts patients in a professional and friendly manner to arrange for payments, as small as $15 per month, encouraging them to pay all monies owed.</p>

    <svg class="court-photo" viewBox="0 0 380 200" role="img" aria-label="Photograph of brass scales of justice and a wooden gavel on a desk">
      <defs>
        <linearGradient id="courtTone" x1="0" y1="0" x2="1" y2="1">
          <stop offset="0" stop-color="#d9c19a"/>
          <stop offset=".45" stop-color="#c29a5a"/>
          <stop offset="1" stop-color="#5a3a20"/>
        </linearGradient>
      </defs>
      <path d="M0 20 Q190 -10 380 30 V200 H0 Z" fill="url(#courtTone)"/>
    </svg>
  </section>

  <section class="panel panel--advisory">
    <div class="navy-edge"></div>
    <h2 class="panel-heading advisory-heading"><span class="accent">Credit Advisory</span> Services</h2>
    <p class="advisory-sub">How well do you really know your customers?</p>
    <p>As an added service to all of our clients, we will draft a customized credit application to be distributed to all of their customers.</p>
    <p>Working closely and alongside their salespeople, we will discretely review and verify the customers' information and investigate all known stakeholders in order to determine creditworthiness.</p>
    <p>As your credit advisor, we will then make a meaningful recommendation with regard to the amount and terms credit should be offered to specific customers.</p>
    <p>Once a credit determination is made, we can provide the client with a credit agreement detailing each parties' obligations. Using such agreements minimizes risk, while enhancing our clients' professional stature with their customers.</p>

    <h2 class="panel-heading advisory-heading ruled"><span><span class="accent">Keeping You</span> In Compliance</span></h2>
    <p>As your collection attorney and advisor, we will assure that your collection practices are in full compliance with all applicable Federal and State laws, including The Fair Debt Collection Practices Act (FDCPA) and The Health Insurance Portability and Accountability Act (HIPAA).</p>

    <h2 class="panel-heading advisory-heading ruled"><span><span class="accent">State-of-the</span> Art Technology</span></h2>
    <p>Our firm prides itself on utilizing the state-of-the-art technology in law office management, telephony, cyber security, document production, and cloud storage.</p>
    <p>Our clients can be assured that their critical business data is stored in a safe, secure, and confidential environment, while allowing us to seamlessly handle a large and ever growing book of business in a timely manner.</p>

    <div class="advisory-band">
      <svg width="380" height="110" viewBox="0 0 380 110">
        <path d="M0 60 Q200 40 380 0 V110 H0 Z" fill="var(--blue-bright)"/>
      </svg>
      <span>www.dornvek.com</span>
    </div>
  </section>

</div>
</body>
</html>
```